Marrowind Booking Engine Marketing Site

Hi,
I’m currently in the process of putting together a web application with the intention of providing small resorts/B&Bs/small hotels the ability to allow their customers to book online.
I’m looking to have a design created for a marketing site, to give potential customers additional information about my booking engine, as well as to help drive sign-ups. A lot of the competition out there appears outdated, so I would like something that is more modern and up to date.
I am looking for just the design (i’m a web developer, but I lack the creative skills for a good marketing site)
For some more background, I will be targeting business owners of smaller resorts and Bed & Breakfasts. These are typically family owned small businesses that may only have a 10 room setup. These businesses will also typically have additional amenities that they will have to rent out or sell to their clients ( ex. Spa, fruit basket, water sport rentals). My software will provide them with the ability to sell their amenities as well.
I’m open to different designs, but my main thing is I want it to look modern, and I want it to have several callouts to sign up for my product.
I am looking to have the homepage created, 1 interior page, and a style guide created (to show form fields, H1’s, etc.).
I had a logo created a couple months ago that will be included with this project brief.
If you need any additional information feel free to reach out to me.

Target Market(s)

This site will be targeted small business owners who are running small resorts, Bed and Breakfasts, or any business that provides rooms for their clients.

Industry/Entity Type

Saas

Number of Pages Required

2 page

Font styles to use
Sans Serif

Colors

Designer to choose colors to be used in the design.

Requirements
Must have
• A modern feel, with several CTA's that will drive to the registration page on the homepage. on the internal page, I mostly just need the page layout, I will reuse that page layout. and a style guide if at all possible (include colors, form fields, H1's, etc.)
Nice to have
• maybe a hero image at the top with buttons over the top? again i'm pretty open to most anything.
Should not have
• I like images, but I don't want the page overrun with images. A good balance.

```html
<!DOCTYPE html>
<html lang="en">
<head>
<meta charset="utf-8">
<title>Marrowind Booking Engine</title>
<link rel="stylesheet" href="https://fonts.googleapis.com/css2?family=Montserrat:wght@300;400;500;600;700&display=swap">
<style>
:root{
  --blue:#1d84f5;
  --green:#8bc53f;
  --ink:#24263a;
  --text:#55586a;
  --muted:#a3a6b0;
  --light:#f4f4f4;
  --line:#d9dbe0;
  --white:#ffffff;
  --frame:#1b1c22;
}
*{margin:0;padding:0;box-sizing:border-box}
html,body{width:1200px;height:2432px;overflow:hidden}
body{position:relative;font-family:"Montserrat",sans-serif;color:var(--ink);background:var(--white)}
.btn{position:absolute;display:flex;align-items:center;justify-content:center;background:var(--blue);color:var(--white);font-weight:700;font-size:12px;border-radius:20px;text-decoration:none;z-index:3}
.brand{position:absolute;display:flex;align-items:center;gap:8px;font-weight:600;font-size:17px;line-height:1;color:var(--blue);z-index:3}
.brand .dot{width:20px;height:20px;border-radius:50%;background:var(--green)}
.brand small{display:block;font-size:11px;font-weight:600;letter-spacing:.5px}

/* header + hero */
.hero{position:absolute;left:0;top:0;width:1200px;height:482px;background:linear-gradient(180deg,#ffffff 0%,#eeeff1 100%)}
.nav a{position:absolute;top:23px;font-size:11px;font-weight:600;color:var(--ink);text-decoration:none;z-index:3}
.nav .active{border-bottom:2px solid var(--blue);padding-bottom:9px}
.hero h1{position:absolute;left:258px;top:178px;font-size:25px;font-weight:400;z-index:2}
.hero .lead{position:absolute;left:258px;top:211px;width:365px;font-size:12.5px;line-height:17px;font-weight:500;z-index:2}
.features{position:absolute;left:258px;top:264px;list-style:none;z-index:2}
.features li{display:flex;align-items:center;gap:12px;height:20px;font-size:10.5px;font-weight:500}
.features svg{width:12px;height:12px}
.tablet{position:absolute;left:0;top:0;z-index:1}
.scroll{position:absolute;left:585px;top:423px;width:30px;height:30px;border-radius:50%;background:var(--blue);display:flex;align-items:center;justify-content:center;z-index:3}

/* how it works */
.section-label{position:absolute;width:1200px;text-align:center;font-size:12px;font-weight:500;letter-spacing:1px}
.step{position:absolute;top:575px;width:170px;text-align:center}
.step .icon{width:66px;height:66px;margin:0 auto;border:1.5px solid #4a4c5a;border-radius:50%;display:flex;align-items:center;justify-content:center;background:var(--white)}
.step h3{margin-top:9px;font-size:10px;font-weight:500}
.step p{margin-top:6px;font-size:8.5px;line-height:11px;color:var(--text)}
.rail{position:absolute;left:157px;top:598px}

/* laptop */
.laptop{position:absolute;left:279px;top:811px;width:637px;height:446px;border-radius:22px 22px 0 0;background:#f0f0f0}
.laptop .screen{position:absolute;left:25px;top:33px;width:587px;height:398px;background:linear-gradient(160deg,#ffffff 0%,#f3f4f6 45%,#caa590 100%)}
.laptop-base{position:absolute;left:170px;top:1245px;width:850px;height:14px;border-radius:0 0 40px 40px;background:linear-gradient(180deg,#e9e9ea,#cfcfd1)}

/* testimonials */
.testimonials{position:absolute;left:0;top:1270px;width:1200px;height:567px;background:var(--light)}
.heading{position:absolute;width:1200px;text-align:center;font-weight:400}
.quote{position:absolute;top:1521px;width:240px;text-align:center}
.quote .avatar{width:42px;height:42px;border-radius:50%;margin:0 auto;background:linear-gradient(135deg,#8a8f99,#3e424c)}
.quote h4{margin-top:15px;font-size:11px;font-weight:500}
.quote .handle{margin-top:7px;font-size:9px;color:var(--muted);letter-spacing:1px}
.quote p{margin-top:18px;font-size:11px;line-height:19px;color:var(--text)}
.pager{position:absolute;left:557px;top:1789px;display:flex;gap:5px}
.pager span{width:6px;height:6px;border-radius:50%;border:1px solid #c8cad0}
.pager span.on{background:#9a9da6;border-color:#9a9da6}

/* newsletter */
.signup label{position:absolute;left:318px;top:2040px;font-size:10px;letter-spacing:2px;color:var(--muted)}
.signup .field{position:absolute;left:305px;top:2063px;width:386px;height:34px;border-radius:18px;background:#f0f0f0;padding-left:16px;display:flex;align-items:center;font-size:10px;color:#c4c6cc}

/* footer */
.footer{position:absolute;left:0;top:2184px;width:1200px;height:248px;background:var(--blue);color:var(--white)}
.footer nav a{position:absolute;top:64px;font-size:12px;font-weight:600;color:var(--white);text-decoration:none;letter-spacing:.5px}
.social span{position:absolute;top:66px;width:12px;height:12px;border-radius:50%;background:var(--white)}
.footer .copy{position:absolute;left:84px;top:169px;font-size:11px}
.footer .legal{position:absolute;top:169px;font-size:10px;letter-spacing:1px;color:#a9d0fb;text-decoration:none}
</style>
</head>
<body>

<header class="hero">
  <svg class="tablet" width="1200" height="540" viewBox="0 0 1200 540" role="img" aria-label="Tablet showing the booking engine dashboard with hotel room photos">
    <defs>
      <linearGradient id="screenTone" x1="0" y1="0" x2="1" y2="1">
        <stop offset="0" stop-color="#ffffff"/>
        <stop offset="0.55" stop-color="#eef0f3"/>
        <stop offset="1" stop-color="#c9a58c"/>
      </linearGradient>
      <filter id="drop" x="-10%" y="-10%" width="130%" height="140%">
        <feDropShadow dx="0" dy="22" stdDeviation="16" flood-color="#000" flood-opacity="0.18"/>
      </filter>
    </defs>
    <polygon points="612,264 1072,64 1210,110 1210,432 770,524 506,352" fill="var(--frame)" filter="url(#drop)"/>
    <polygon points="628,270 1070,78 1210,124 1210,420 772,508 528,352" fill="url(#screenTone)"/>
  </svg>

  <div class="brand" style="left:259px;top:16px"><span class="dot"></span><span>MARROWIND<small>BOOKING ENGINE</small></span></div>
  <nav class="nav">
    <a class="active" href="#" style="left:687px">About</a>
    <a href="#" style="left:736px">How it Works</a>
    <a href="#" style="left:823px">Plans</a>
  </nav>
  <a class="btn" href="#" style="left:874px;top:13px;width:118px;height:33px">Get Started</a>

  <h1>Manager of a Hotel or BnB?</h1>
  <p class="lead">Marrowind Booking Engine is a fresh online booking system that saves our customers 1.5h/day on average!</p>
  <ul class="features">
    <li><svg viewBox="0 0 12 12"><circle cx="6" cy="6" r="5" fill="none" stroke="#8bc53f"/><path d="M3.5 6l1.8 1.8L8.6 4.4" fill="none" stroke="#8bc53f" stroke-width="1.2"/></svg>Booking Management</li>
    <li><svg viewBox="0 0 12 12"><circle cx="6" cy="6" r="5" fill="none" stroke="#8bc53f"/><path d="M3.5 6l1.8 1.8L8.6 4.4" fill="none" stroke="#8bc53f" stroke-width="1.2"/></svg>Property Management</li>
    <li><svg viewBox="0 0 12 12"><circle cx="6" cy="6" r="5" fill="none" stroke="#8bc53f"/><path d="M3.5 6l1.8 1.8L8.6 4.4" fill="none" stroke="#8bc53f" stroke-width="1.2"/></svg>Content Management System (CMS)</li>
  </ul>
  <a class="btn" href="#" style="left:259px;top:363px;width:130px;height:33px">Join Marrowind</a>
  <div class="scroll"><svg width="12" height="8" viewBox="0 0 12 8"><path d="M1 1.5l5 5 5-5" fill="none" stroke="#fff" stroke-width="2"/></svg></div>
</header>

<section class="how">
  <div class="section-label" style="top:538px">HOW IT WORKS</div>
  <svg class="rail" width="890" height="20" viewBox="0 0 890 20">
    <line x1="0" y1="10" x2="886" y2="10" stroke="#c9ccd2" stroke-dasharray="2 3"/>
    <g fill="#fff" stroke="#8bc53f" stroke-width="1.5">
      <circle cx="44" cy="10" r="7"/><circle cx="134" cy="10" r="7"/><circle cx="221" cy="10" r="7"/>
      <circle cx="311" cy="10" r="7"/><circle cx="398" cy="10" r="7"/><circle cx="488" cy="10" r="7"/>
      <circle cx="575" cy="10" r="7"/><circle cx="665" cy="10" r="7"/><circle cx="752" cy="10" r="7"/><circle cx="842" cy="10" r="7"/>
    </g>
  </svg>
  <div class="step" style="left:72px"><div class="icon"><svg width="30" height="30" viewBox="0 0 30 30" fill="none" stroke="#24263a" stroke-width="1.8"><rect x="4" y="4" width="22" height="22"/><path d="M9 20V13l6-5 6 5v7z"/></svg></div><h3>Dashboard</h3><p>Get a quick overview of incoming guests and upcoming checkouts. You can also check in/check out customers and go straight to the payment module.</p></div>
  <div class="step" style="left:249px"><div class="icon"><svg width="30" height="30" viewBox="0 0 30 30" fill="none" stroke="#24263a" stroke-width="1.8"><rect x="4" y="6" width="22" height="20" rx="3"/><path d="M4 12h22M10 3v5M20 3v5"/><text x="15" y="23" font-size="9" font-family="Montserrat,sans-serif" text-anchor="middle" fill="#24263a" stroke="none" font-weight="700">23</text></svg></div><h3>Calendar</h3><p>An overview of all your objects and guests. Here you can also find quick access to bills and customer information through a few clicks.</p></div>
  <div class="step" style="left:427px"><div class="icon"><svg width="30" height="30" viewBox="0 0 30 30" fill="none" stroke="#24263a" stroke-width="1.8"><rect x="4" y="5" width="22" height="20"/><rect x="9" y="10" width="12" height="10"/></svg></div><h3>Book</h3><p>Booking of guests through the administration interface, and creates a bill that the customer can pay on site.</p></div>
  <div class="step" style="left:604px"><div class="icon"><svg width="30" height="30" viewBox="0 0 30 30" fill="none" stroke="#24263a" stroke-width="1.8"><rect x="4" y="4" width="22" height="22"/><path d="M10 21v-5M14 21v-8M18 21v-6M22 21V9" stroke-width="2.4"/></svg></div><h3>Economy in Harmony</h3><p>Filtering function for easy access to the bills you are searching for.</p></div>
  <div class="step" style="left:781px"><div class="icon"><svg width="30" height="30" viewBox="0 0 30 30"><path d="M16 4h9v9L14 24l-9-9z" fill="#24263a"/><circle cx="21" cy="8" r="2" fill="#fff"/></svg></div><h3>Campaigns and Events</h3><p>Get a quick overview of your current and upcoming campaigns with a dynamic pricing module.</p></div>
  <div class="step" style="left:958px"><div class="icon"><svg width="30" height="30" viewBox="0 0 30 30" fill="none" stroke="#24263a" stroke-width="1.8"><rect x="8" y="4" width="16" height="20"/><path d="M6 8v18h14M12 10h8M12 14h8M12 18h8"/></svg></div><h3>Statistics and Reports</h3><p>Create reports for occupancy, guests and lists of rooms that should be cleaned.</p></div>
  <a class="btn" href="#" style="left:535px;top:749px;width:130px;height:34px">Join Marrowind</a>
</section>

<div class="laptop"><div class="screen" role="img" aria-label="Booking engine rooms screen with hotel room photographs"></div></div>
<div class="laptop-base"></div>

<section class="testimonials"></section>
<div class="section-label" style="top:1332px;font-size:10px;color:var(--muted);letter-spacing:2px">TESTIMONIALS</div>
<h2 class="heading" style="top:1361px;font-size:24px">People Really Like Marrowind Booking</h2>
<p class="heading" style="top:1393px;font-size:15px;color:var(--text);font-weight:300">But don't take our word for it...</p>
<div class="quote" style="left:191px"><div class="avatar" role="img" aria-label="Portrait of Dorian Webb"></div><h4>Dorian Webb</h4><div class="handle">@DWEBB</div><p>Looking cautiously round, to ascertain that they were not overheard, the two hags cowered nearer to the fire, and chuckled heartily.</p></div>
<div class="quote" style="left:480px"><div class="avatar" role="img" aria-label="Portrait of Milo Hartley"></div><h4>Milo Hartley</h4><div class="handle">@HARTLEYMILO</div><p>Just then her head struck against the roof of the hall: in fact she was now more than nine feet high, and she at once took up the little golden key and hurried off to the garden door.</p></div>
<div class="quote" style="left:767px"><div class="avatar" role="img" aria-label="Portrait of Celia Thornton"></div><h4>Celia Thornton</h4><div class="handle">@CELIAT</div><p>She gave my mother such a turn, that I have always been convinced I am indebted to Miss Betsey for having been born on a Friday.</p></div>
<div class="pager"><span class="on"></span><span></span><span></span><span></span><span></span><span></span><span></span></div>

<section class="signup">
  <h2 class="heading" style="top:1899px;font-size:24px">Ready to Start?</h2>
  <p class="heading" style="top:1946px;font-size:16px;line-height:25px;color:var(--text);font-weight:300">Subscribe to our newsletters to learn more about<br>Marrowind Booking Engine updates.</p>
  <label>YOUR E-MAIL</label>
  <div class="field">name@mail.com</div>
  <a class="btn" href="#" style="left:725px;top:2062px;width:170px;height:36px;font-size:11px;letter-spacing:1px">GET STARTED</a>
</section>

<footer class="footer">
  <div class="brand" style="left:102px;top:58px;color:#fff"><span class="dot" style="background:#fff"></span><span>MARROWIND<small>BOOKING ENGINE</small></span></div>
  <nav>
    <a href="#" style="left:451px">ABOUT</a>
    <a href="#" style="left:512px">HOW IT WORKS</a>
    <a href="#" style="left:627px">PLANS</a>
    <a href="#" style="left:685px">CONTACTS</a>
  </nav>
  <div class="social"><span style="left:1029px"></span><span style="left:1063px"></span><span style="left:1098px"></span></div>
  <p class="copy">© Copyright 2018 Marrowind Booking Engine - All Rights Reserved</p>
  <a class="legal" href="#" style="left:832px">PRIVACY POLICY</a>
  <a class="legal" href="#" style="left:963px">TERMS AND CONDITIONS</a>
</footer>

</body>
</html>
```